Hairdressing Salon called; Tressel Studio. Style Is Us

Tressel Studio
We Love Hair
418 Wexbury Lane Hollin Park
4839172
Business card not to fussy.
I would like it to be a Black background with White and/or Grey lettering.

I really like the business card attached, so if the front looked like this I would be really happy, but would also like my address and phone number on the front.

On the back I would like two options of
1: reward card; buy any Haircare product over $20 on any visit and on the tenth product receive a complimentry Treatment and
2: appointment times and date

Business

Tressel Studio
We Love Hair
4839172
418 Wexbury Lane, Hollin Park
This must all be included on the front of the card

Serif
Decorative
Script

1b1b1b
757575
ffffff

Must have
• My phone number and address
Should not have
• Pictures on the front

```html
<!DOCTYPE html>
<html lang="en">
<head>
<meta charset="utf-8">
<title>Tressel Studio — Business Card</title>
<link rel="stylesheet" href="https://fonts.googleapis.com/css2?family=Cinzel:wght@400;600&family=Oswald:wght@500;600&display=swap">
<style>
  :root {
    --ink-black: #0d0d0d;
    --card-black: #1b1b1b;
    --mid-grey: #757575;
    --soft-grey: #9a9a9a;
    --white: #ffffff;
    --page: #f4f4f4;
    --card-w: 567px;
    --card-h: 401px;
  }
  * { margin: 0; padding: 0; box-sizing: border-box; }
  html, body { width: 1200px; height: 454px; overflow: hidden; background: var(--page); }
  .canvas { position: relative; width: 1200px; height: 454px; }

  .card { position: absolute; top: 26px; width: var(--card-w); height: var(--card-h); }
  .card--front { left: 19px; }
  .card--back { left: 615px; }
  .card-shape { position: absolute; inset: 0; width: 100%; height: 100%; }

  /* Front */
  .ornament {
    position: absolute; left: 50%; transform: translateX(-50%);
    border-radius: 40px;
    background: radial-gradient(ellipse at center, rgba(255,255,255,0.28), rgba(255,255,255,0) 70%);
  }
  .ornament--top { top: 112px; width: 200px; height: 34px; }
  .ornament--bottom { top: 200px; width: 220px; height: 30px; }
  .brand-name {
    position: absolute; top: 146px; width: 100%; text-align: center;
    font-family: 'Cinzel', serif; font-weight: 400; font-size: 25px;
    letter-spacing: 6px; color: var(--white);
  }
  .brand-tagline {
    position: absolute; top: 180px; width: 100%; text-align: center;
    font-family: 'Cinzel', serif; font-weight: 400; font-size: 15px;
    letter-spacing: 2px; color: var(--soft-grey);
  }
  .contact { position: absolute; top: 280px; width: 100%; text-align: center; color: var(--white);
    font-family: 'Oswald', sans-serif; font-weight: 600; }
  .contact-phone { font-size: 20px; letter-spacing: 4px; margin-bottom: 16px; }
  .contact-address { font-size: 17px; line-height: 22px; letter-spacing: 1px; }

  /* Back */
  .stamp-grid {
    position: absolute; left: 43px; top: 48px; width: 482px;
    display: grid; grid-template-columns: repeat(5, 1fr); gap: 14px 8px;
  }
  .stamp-box {
    height: 143px; position: relative;
    background: linear-gradient(180deg, #8a8a8a, var(--mid-grey));
  }
  .stamp-fields {
    position: absolute; left: 6px; bottom: 6px;
    font-family: 'Oswald', sans-serif; font-weight: 500; font-size: 10px;
    line-height: 13px; color: var(--white); letter-spacing: 0.5px;
  }
  .reward-note {
    position: absolute; right: 42px; top: 360px; text-align: right;
    font-family: 'Oswald', sans-serif; font-weight: 500; font-size: 12px;
    line-height: 15px; color: var(--white); letter-spacing: 0.4px; text-transform: uppercase;
  }
</style>
</head>
<body>
<main class="canvas">

  <section class="card card--front" aria-label="Card front">
    <svg class="card-shape" viewBox="0 0 567 401" aria-hidden="true">
      <defs>
        <radialGradient id="front-glow" cx="50%" cy="42%" r="65%">
          <stop offset="0" stop-color="#3a3a3a"/>
          <stop offset="0.55" stop-color="#1b1b1b"/>
          <stop offset="1" stop-color="#050505"/>
        </radialGradient>
      </defs>
      <path d="M22,0 H545 A22,22 0 0 0 567,22 V379 A22,22 0 0 0 545,401 H22 A22,22 0 0 0 0,379 V22 A22,22 0 0 0 22,0 Z" fill="url(#front-glow)"/>
      <path d="M30,10 H537 A20,20 0 0 0 557,30 V371 A20,20 0 0 0 537,391 H30 A20,20 0 0 0 10,371 V30 A20,20 0 0 0 30,10 Z" fill="none" stroke="#ffffff" stroke-width="1.5"/>
    </svg>
    <div class="ornament ornament--top" role="img" aria-label="Decorative scroll flourish above the name"></div>
    <h1 class="brand-name">TRESSEL STUDIO</h1>
    <p class="brand-tagline">STYLE IS US</p>
    <div class="ornament ornament--bottom" role="img" aria-label="Decorative scroll flourish below the tagline"></div>
    <div class="contact">
      <p class="contact-phone">4839172</p>
      <p class="contact-address">418 WEXBURY LANE<br>HOLLIN PARK</p>
    </div>
  </section>

  <section class="card card--back" aria-label="Card back: reward and appointment card">
    <svg class="card-shape" viewBox="0 0 567 401" aria-hidden="true">
      <defs>
        <radialGradient id="back-glow" cx="50%" cy="50%" r="62%">
          <stop offset="0" stop-color="#5a5a5a"/>
          <stop offset="0.5" stop-color="#262626"/>
          <stop offset="1" stop-color="#080808"/>
        </radialGradient>
      </defs>
      <path d="M22,0 H545 A22,22 0 0 0 567,22 V379 A22,22 0 0 0 545,401 H22 A22,22 0 0 0 0,379 V22 A22,22 0 0 0 22,0 Z" fill="url(#back-glow)"/>
      <path d="M30,10 H537 A20,20 0 0 0 557,30 V371 A20,20 0 0 0 537,391 H30 A20,20 0 0 0 10,371 V30 A20,20 0 0 0 30,10 Z" fill="none" stroke="#ffffff" stroke-width="1.5"/>
    </svg>
    <div class="stamp-grid">
      <div class="stamp-box"><p class="stamp-fields">TIME:<br>DATE:</p></div>
      <div class="stamp-box"><p class="stamp-fields">TIME:<br>DATE:</p></div>
      <div class="stamp-box"><p class="stamp-fields">TIME:<br>DATE:</p></div>
      <div class="stamp-box"><p class="stamp-fields">TIME:<br>DATE:</p></div>
      <div class="stamp-box"><p class="stamp-fields">TIME:<br>DATE:</p></div>
      <div class="stamp-box"><p class="stamp-fields">TIME:<br>DATE:</p></div>
      <div class="stamp-box"><p class="stamp-fields">TIME:<br>DATE:</p></div>
      <div class="stamp-box"><p class="stamp-fields">TIME:<br>DATE:</p></div>
      <div class="stamp-box"><p class="stamp-fields">TIME:<br>DATE:</p></div>
      <div class="stamp-box"><p class="stamp-fields">TIME:<br>DATE:</p></div>
    </div>
    <p class="reward-note">Buy any hair product over $20 for each stamp,<br>10th stamp will get complimentary treatment.</p>
  </section>

</main>
</body>
</html>
```